Tradolo - Forex Signal Services Moments Matter Most. Shape your future.

I need an attractive eye catching web design that is azure friendly. I currently have a web programmer working on the backend of my website. Now I need a professional design to attract and retain customers. This site needs to be mobile friendly.

Tradolo is a highly reputable, trustworthy and professional site that offers forex signals to traders in all parts of the globe. With accurate and reliable forex signals, traders can not only make money but also boost their profits.

At Tradolo, we want our clients to have complete faith on us and our services! We also do not want our users to lead a simple and monotonous life. Instead our goal is to help them create an extra source of steady income. However, this is possible only when our clients resolve to change their lives for the better. They need to change their mindset and most importantly develop a positive frame of mind. That’s exactly why at Tradolo, we provide our clients with innumerable personal development tools and resources that’ll aid them in changing all the aspects of their lives. We want our traders to feel inspired and educate them in the right way!

Colors are flexible.

I do like the simplicity of www.brightmarkvo.example.
I do want a design more professional in appearance and not everything on page one.

I have not been able to decide on a logo. There is one of lower quality as I have not paid for it yet but I will if you decide it's the best for my business I will. Or should one feel that they have a better idea for a logo, I will pay for it if i like it.

I have included some of the content of my site so you can get a feel for where I am coming from.
(Please note that this content is still in the editing process)
Updates

Project Deadline Extended Reason: My content was not complete nor finalization of the final logo. We will allow a few more days for designers to modify the website.Thank you for your patience and understanding. Added Tuesday, January 24, 2017

Target Market(s)

I work with Forex Traders, Investors wanting to control their own portfolios, and remote nomads/mellienials

Coding

Number of Pages Required

Requirements
Must have
• I must have a professional clean look. I want the site to be interactive and eye catching. I want my audience hooked within seconds of opening it. It has to have all important information first. Photos must be legit and not spammy. I work as a representative in the financial market. I want my site to reflect that I stand by my product and reputation means everything to me. This site has to be engaging.
• Sorry, I should have included this earlier of what I will all need on this site.
• I'll have about Tradolo (my company, what we stand for, who we work with, my strategy, etc....
• about me (why i started this company, who I am)
• Performance (graphs and recent posts of signals)
• Membership (how to sign up)
• Terms of service/legal/disclaimers
• FAQS
• Personal Development Resources
• Forex Education Resources
Nice to have
• Quick links to bounce around the site faster.
Should not have
• I do not want over the top white collar conservative.

```html
<!DOCTYPE html>
<html lang="en">
<head>
<meta charset="utf-8">
<title>Tradolo - Forex Signal Services</title>
<link rel="stylesheet" href="https://fonts.googleapis.com/css2?family=Open+Sans:wght@400;600;700&family=Roboto:wght@400;500;700&family=Roboto+Condensed:wght@400;700&display=swap">
<style>
:root{
  --teal:#3aa89e;
  --teal-dark:#2f8f86;
  --orange:#f07a22;
  --blue:#3c84cb;
  --blue-dark:#2f6fb3;
  --ink:#2b2b2b;
  --text:#666;
  --muted:#8a8a8a;
  --line:#dcdcdc;
  --soft:#f3f3f3;
  --card:#f7f8fa;
  --dark:#2a2c30;
  --darker:#1d1e21;
  --white:#fff;
  --accent-red:#d9342b;
}
*{box-sizing:border-box;margin:0;padding:0}
html,body{width:1200px;height:3636px;overflow:hidden}
body{font-family:"Open Sans",sans-serif;color:var(--text);background:var(--white);font-size:13px;line-height:1.7}
.wrap{width:1006px;margin:0 auto;position:relative}
h2.section-title{font-family:"Roboto",sans-serif;font-weight:500;font-size:29px;color:var(--ink);text-align:center;letter-spacing:.5px}
.btn{display:inline-block;border:1px solid #999;border-radius:3px;padding:6px 12px;font-family:"Roboto",sans-serif;font-size:11px;font-weight:500;color:#444;letter-spacing:.5px;text-transform:uppercase}
.btn-light{border-color:rgba(255,255,255,.8);color:var(--white);padding:8px 22px;font-size:13px}

/* header */
.site-header{height:110px;position:relative}
.brand{position:absolute;left:0;top:18px;display:flex;align-items:center;gap:10px}
.brand-dot{width:30px;height:30px;border-radius:50%;background:var(--orange)}
.brand-name{font-family:"Open Sans",sans-serif;font-weight:600;font-size:24px;color:#444;letter-spacing:1px}
.contact-bar{position:absolute;right:0;top:16px;display:flex;gap:40px;font-size:14px;color:#444}
.contact-bar span{display:flex;align-items:center;gap:10px}
.ic-round{width:28px;height:28px;border:1.5px solid #555;border-radius:50%;display:flex;align-items:center;justify-content:center}
.main-nav{position:absolute;right:0;top:68px;display:flex;gap:38px;font-family:"Roboto",sans-serif;font-size:13px;font-weight:500;color:#444;text-transform:uppercase}
.main-nav a.active{color:var(--accent-red);border-bottom:2px solid var(--accent-red);padding-bottom:8px}

/* hero */
.hero{height:532px;background:linear-gradient(180deg,#3fb0a5,#35a096);position:relative;overflow:hidden}
.hero-copy{position:absolute;left:97px;top:182px;color:var(--white)}
.hero-copy h1{font-family:"Roboto",sans-serif;font-weight:700;font-size:48px;line-height:1}
.hero-copy .tag{font-family:"Roboto",sans-serif;font-weight:500;font-size:27px;margin-top:10px;text-transform:uppercase}
.hero-copy p{font-size:15px;line-height:1.45;margin-top:14px}
.dots{display:flex;gap:6px;margin-top:20px}
.dots i{width:13px;height:13px;border-radius:50%;border:2px solid var(--white)}
.dots i.on{background:#f5b819;border-color:#f5b819}
.hero-art{position:absolute;left:418px;top:0;width:782px;height:532px;background:radial-gradient(ellipse at 55% 55%,#6fcac0 0%,#47b4a9 50%,rgba(58,168,158,0) 80%)}

/* welcome */
.welcome{height:263px;background:var(--soft);text-align:center;padding-top:45px}
.welcome p{width:1006px;margin:22px auto 20px;font-size:12px;line-height:1.75}

/* services */
.services{height:585px;padding-top:82px;text-align:center}
.services .lead{width:820px;margin:18px auto 0;font-size:12px;line-height:1.7}
.cards{display:flex;gap:29px;margin-top:48px}
.card{width:316px;height:280px;background:var(--card);border:1px solid #e5e7ea;box-shadow:0 6px 10px -6px rgba(0,0,0,.18);padding-top:36px}
.card .badge{width:74px;height:74px;border-radius:50%;background:var(--orange);margin:0 auto;display:flex;align-items:center;justify-content:center}
.card h3{font-family:"Roboto",sans-serif;font-weight:400;font-size:17px;color:#333;text-transform:uppercase;margin-top:20px}
.card p{font-size:11.5px;line-height:1.6;margin:10px 40px 0}
.card .more{display:inline-block;margin-top:16px;font-family:"Roboto",sans-serif;font-size:12px;font-weight:500;color:#333}

/* investors */
.investors{height:390px;background:linear-gradient(135deg,#4a93d6,var(--blue) 45%,var(--blue-dark));color:var(--white);text-align:center;padding-top:70px}
.investors h2{font-family:"Roboto",sans-serif;font-weight:500;font-size:30px;text-transform:uppercase}
.investors p{width:1006px;margin:18px auto 0;font-size:12px;line-height:1.75}
.investors p+p{margin-top:14px}
.investors .btn{margin-top:16px}

/* benefits */
.benefits{height:545px;position:relative}
.monitor{position:absolute;left:133px;top:80px;width:390px;height:340px}
.monitor .screen{position:absolute;left:0;top:0;width:390px;height:262px;border:10px solid #222;border-bottom-width:28px;border-radius:6px;background:linear-gradient(135deg,#7a93a8,#c9d3dc 55%,#8ea0b0)}
.monitor .stand{position:absolute;left:160px;top:262px;width:70px;height:60px;background:linear-gradient(#d6d6d6,#b9b9b9)}
.monitor .foot{position:absolute;left:120px;top:318px;width:150px;height:10px;border-radius:5px;background:#c7c7c7}
.benefit-copy{position:absolute;left:589px;top:68px;width:480px}
.benefit-copy h2{font-family:"Roboto",sans-serif;font-weight:500;font-size:28px;color:var(--ink);text-transform:uppercase}
.benefit-copy .lead{font-size:11.5px;line-height:1.6;margin-top:12px}
.point{display:flex;gap:16px;margin-top:20px}
.point .icon{flex:none;width:52px;height:52px;border:1.5px solid #444;border-radius:50%;display:flex;align-items:center;justify-content:center}
.point h4{font-family:"Roboto",sans-serif;font-weight:400;font-size:15px;color:#333;text-transform:uppercase}
.point p{font-size:11.5px;line-height:1.6}

/* testimonials */
.testimonials{height:335px;background:linear-gradient(135deg,#34373c,var(--dark) 50%,#222427);color:var(--white);text-align:center;padding-top:62px}
.testimonials h2{font-family:"Roboto",sans-serif;font-weight:500;font-size:29px;text-transform:uppercase}
.testimonials blockquote{width:1006px;margin:20px auto 0;font-size:12.5px;line-height:1.75}
.testimonials cite{display:block;margin-top:14px;font-family:"Roboto",sans-serif;font-style:italic;font-size:17px}
.testimonials cite small{font-size:12px}
.bar-dots{display:flex;gap:6px;justify-content:center;margin-top:14px}
.bar-dots i{width:24px;height:3px;background:#666}
.bar-dots i.on{background:var(--white)}

/* blog */
.blog{height:530px;padding-top:64px}
.posts{display:flex;gap:29px;margin-top:38px}
.post{width:316px}
.post .thumb{height:180px;position:relative}
.post .date{position:absolute;left:0;bottom:0;width:48px;height:82px;background:#333;color:var(--white);font-family:"Roboto",sans-serif;font-size:12px;line-height:1.2;text-align:center;padding-top:14px}
.post h3{font-family:"Roboto",sans-serif;font-weight:400;font-size:17px;color:#333;margin-top:18px}
.post p{font-size:11.5px;line-height:1.6;margin-top:8px}
.post .btn{margin-top:14px}

/* footer */
.site-footer{height:341px;background:var(--darker);color:#ccc;position:relative}
.footer-cols{display:flex;padding-top:88px}
.footer-cols h4{font-family:"Roboto",sans-serif;font-weight:400;font-size:16px;color:var(--white);text-transform:uppercase}
.col-news{width:346px}
.col-news p{font-size:11.5px;line-height:1.5;margin-top:12px;width:230px}
.field{width:245px;height:40px;background:var(--white);margin-top:12px;font-size:11px;color:#888;padding:10px 10px}
.sub-btn{display:inline-block;margin-top:14px;background:var(--orange);color:var(--white);font-size:11px;padding:8px 12px;text-transform:uppercase}
.col-contact{width:325px}
.col-contact li{list-style:none;display:flex;gap:14px;font-size:11.5px;line-height:1.5;margin-top:14px}
.col-links{width:200px}
.col-links li{list-style:none;font-size:11.5px;line-height:2.1}
.col-links ul{margin-top:10px}
.col-brand{flex:1;display:flex;flex-direction:column;align-items:center;padding-top:20px}
.col-brand .brand-name{color:var(--white);font-size:26px}
.col-brand .brand-dot{width:40px;height:40px;margin-bottom:10px}
.socials{display:flex;gap:8px;margin-top:20px}
.socials i{width:26px;height:26px;border:1.5px solid #ddd;border-radius:50%}
.copyright{position:absolute;left:0;right:0;bottom:0;height:60px;border-top:1px solid #333;text-align:center;font-size:11px;color:#aaa;padding-top:22px}
</style>
</head>
<body>

<header class="site-header">
  <div class="wrap">
    <div class="brand"><span class="brand-dot"></span><span class="brand-name">Tradolo</span></div>
    <div class="contact-bar">
      <span><i class="ic-round"><svg width="14" height="14" viewBox="0 0 24 24"><path d="M6.6 10.8a15 15 0 0 0 6.6 6.6l2.2-2.2a1 1 0 0 1 1-.25 11.4 11.4 0 0 0 3.6.6 1 1 0 0 1 1 1V20a1 1 0 0 1-1 1A17 17 0 0 1 3 4a1 1 0 0 1 1-1h3.5a1 1 0 0 1 1 1c0 1.25.2 2.45.6 3.6a1 1 0 0 1-.25 1z" fill="#444"/></svg></i>900 0000 1234</span>
      <span><i class="ic-round"><svg width="14" height="14" viewBox="0 0 24 24"><rect x="3" y="6" width="18" height="12" fill="none" stroke="#444" stroke-width="2"/><path d="M3 6l9 7 9-7" fill="none" stroke="#444" stroke-width="2"/></svg></i>info@tradolo.example</span>
    </div>
    <nav class="main-nav">
      <a class="active">Home</a><a>About Us</a><a>Our Services</a><a>Blog</a><a>Contact Us</a>
    </nav>
  </div>
</header>

<section class="hero">
  <div class="hero-art" role="img" aria-label="Illustration of hands using a laptop, tablet and phone showing trading charts over a world map with floating coins"></div>
  <div class="hero-copy">
    <h1>TRADOLO</h1>
    <div class="tag">Shape your future</div>
    <p>Lorem ipsum dolor sit amet, consectetur<br>Sed ut perspiciatis unde sed</p>
    <div class="dots"><i class="on"></i><i></i><i></i></div>
  </div>
</section>

<section class="welcome">
  <h2 class="section-title">WELCOME TO TRADOLO.COM!</h2>
  <p>Pardon my language but there is a lot of noise on the internet, especially when it comes to the services I offer. I have spent countless hours and years of my life towards my passion for the currency industry. I finally developed a strategy I am proud of and stand by my product with my name and company brand. I wholeheartedly believe that the extent of our personal success is a measure of accomplishments we have helped others create. I want people to succeed.</p>
  <span class="btn">Read More &#9656;</span>
</section>

<section class="services">
  <div class="wrap">
    <h2 class="section-title">FOREX SIGNAL SERVICES</h2>
    <p class="lead">We use proven strategies to help traders in succeeding in the forex market. Our forex experts provide high-probability, professional and consistent forex signals and charts that help traders in maximizing their profits and eliminating losses. Try our free Currency Education service.</p>
    <div class="cards">
      <article class="card">
        <div class="badge"><svg width="36" height="36" viewBox="0 0 36 36"><circle cx="18" cy="18" r="14" fill="#fff"/><path d="M18 18V4a14 14 0 0 1 14 14z" fill="#f07a22" stroke="#fff" stroke-width="2"/></svg></div>
        <h3>Our Strategy</h3>
        <p>Tradolo.com works with both day as well as intraday traders. We only hold a maximum of one position at any given point in time. Once we've</p>
        <span class="more">READ MORE &#10148;</span>
      </article>
      <article class="card">
        <div class="badge"><svg width="38" height="38" viewBox="0 0 38 38"><circle cx="19" cy="14" r="10" fill="#fff"/><text x="19" y="19" text-anchor="middle" font-family="Roboto,sans-serif" font-weight="700" font-size="14" fill="#f07a22">$</text><path d="M4 30c6-4 12-4 16-2h8c2 0 2 3 0 3h-8M4 34h20l10-6" fill="none" stroke="#fff" stroke-width="2.4" stroke-linecap="round"/></svg></div>
        <h3>Why Us?</h3>
        <p>Put simply, because we're different! We are a "Never before Seen" forex trading company that is focused on guiding, mentoring and assisting</p>
        <span class="more">READ MORE &#10148;</span>
      </article>
      <article class="card">
        <div class="badge"><svg width="36" height="36" viewBox="0 0 36 36"><circle cx="18" cy="8" r="5" fill="#fff"/><rect x="7" y="20" width="5" height="12" fill="#fff"/><rect x="15.5" y="16" width="5" height="16" fill="#fff"/><rect x="24" y="12" width="5" height="20" fill="#fff"/></svg></div>
        <h3>Why Tradolo</h3>
        <p>We're a small company based in the beautiful hills of Pine Hollow, Northridge with over 9 years of successful trading experience</p>
        <span class="more">READ MORE &#10148;</span>
      </article>
    </div>
  </div>
</section>

<section class="investors">
  <h2>Investors and Retirees</h2>
  <p>If you are someone that has been tricked before or have lost your savings to investment companies and would like to know how you can take care of your own investment, then we are here to help you. We will show you how to trade your own money so you can control your own investment. We will get you through the steps towards your goal as quickly as possible. You don't even have to know how trade to be able to take care of your own money. Everything that you need to get you on your way will be provided and explained in detail.</p>
  <p>Please note that we do not require you send us your investment in order to do this. We are only here to show you how you can do this on your own and that you don't need anyone to do this for you. You can learn more about how to take care of your own investment here.</p>
  <span class="btn btn-light">READ MORE</span>
</section>

<section class="benefits">
  <div class="monitor">
    <div class="screen" role="img" aria-label="Photo of hands working on a laptop with documents, shown on a desktop monitor"></div>
    <div class="stand"></div><div class="foot"></div>
  </div>
  <div class="benefit-copy">
    <h2>How will Forex signals help you?</h2>
    <p class="lead">We appeal to Forex Traders, Investors interested in Managing their own portfolios, Remote Nomads, Work from home entrepreneurs and Millenials.</p>
    <div class="point">
      <div class="icon"><svg width="24" height="24" viewBox="0 0 24 24"><path d="M3 20h18M4 16l5-5 4 3 7-7" fill="none" stroke="#444" stroke-width="2"/></svg></div>
      <div><h4>Forex Traders Everywhere</h4><p>Forex Trading is not for the faint hearted. If you have been trading for years, you will know exactly what I am talking about.</p></div>
    </div>
    <div class="point">
      <div class="icon"><svg width="22" height="22" viewBox="0 0 24 24"><path d="M11 3a9 9 0 1 0 9 10h-9z" fill="#444"/><path d="M13 1v10h10A10 10 0 0 0 13 1z" fill="#444"/></svg></div>
      <div><h4>Investors</h4><p>I will show you how you can invest your money and manage it yourself. No need to hire someone else to look after your investment</p></div>
    </div>
    <div class="point">
      <div class="icon"><svg width="22" height="22" viewBox="0 0 24 24"><path d="M3 11l9-8 9 8M5 10v10h14V10" fill="none" stroke="#444" stroke-width="2"/></svg></div>
      <div><h4>Work at Home Entrepreneurs</h4><p>Work At Home has become popular as the internet becomes available to more and more homes around the world</p></div>
    </div>
  </div>
</section>

<section class="testimonials">
  <h2>Testimonials</h2>
  <blockquote>&ldquo; Lorem ipsum dolor sit amet, consectetur adipiscing elit, sed do eiusmod tempor incididunt ut labore et dolore magna aliqua. Ut enim ad minim veniam, quis nostrud exercitation ullamco laboris nisi ut aliquip ex ea commodo consequat. Duis aute irure dolor in reprehenderit in voluptate velit esse cillum dolore eu fugiat nulla Sed ut perspiciatis unde omnis iste natus error sit voluptatem accusantium doloremque laudantium, totam rem aperiam, eaque ipsa quae ab illo inventore veritatis et quasi architecto beatae vitae</blockquote>
  <cite>John Doe <small>- Tradolo</small></cite>
  <div class="bar-dots"><i class="on"></i><i></i><i></i></div>
</section>

<section class="blog">
  <div class="wrap">
    <h2 class="section-title">LATEST BLOG</h2>
    <div class="posts">
      <article class="post">
        <div class="thumb" role="img" aria-label="Photo of a calculator and financial papers on a desk" style="background:linear-gradient(135deg,#b9c7cf,#e7ecef)"><div class="date">SEP<br>09<br>2017</div></div>
        <h3>Nemo enim ipsam voluptatem quia</h3>
        <p>Sed ut perspiciatis unde omnis iste natus error sit uptatem accusantium doloremque laudantium, totam rem aperiam, eaque ipsa quae ab illo inventore veritatis.</p>
        <span class="btn">Read More</span>
      </article>
      <article class="post">
        <div class="thumb" role="img" aria-label="Photo of a pen and printed charts in an office" style="background:linear-gradient(135deg,#d7dde2,#a9b8c4)"><div class="date">SEP<br>09<br>2017</div></div>
        <h3>Nemo enim ipsam voluptatem quia</h3>
        <p>Sed ut perspiciatis unde omnis iste natus error sit uptatem accusantium doloremque laudantium, totam rem aperiam, eaque ipsa quae ab illo inventore veritatis.</p>
        <span class="btn">Read More</span>
      </article>
      <article class="post">
        <div class="thumb" role="img" aria-label="Photo of a business meeting at a bright office table" style="background:linear-gradient(135deg,#e9ecef,#a8b4bf)"><div class="date">SEP<br>09<br>2017</div></div>
        <h3>Nemo enim ipsam voluptatem quia</h3>
        <p>Sed ut perspiciatis unde omnis iste natus error sit uptatem accusantium doloremque laudantium, totam rem aperiam, eaque ipsa quae ab illo inventore veritatis.</p>
        <span class="btn">Read More</span>
      </article>
    </div>
  </div>
</section>

<footer class="site-footer">
  <div class="wrap footer-cols">
    <div class="col-news">
      <h4>Sign up for newsletter</h4>
      <p>Excepteur sint occaecat cupidatat non proident, sunt in culpa qui officia deserunt</p>
      <div class="field">Enter email</div>
      <span class="sub-btn">Subscription</span>
    </div>
    <div class="col-contact">
      <h4>Contact Us</h4>
      <ul>
        <li><svg width="12" height="16" viewBox="0 0 12 16"><path d="M6 0a6 6 0 0 0-6 6c0 4.5 6 10 6 10s6-5.5 6-10a6 6 0 0 0-6-6zm0 8.5A2.5 2.5 0 1 1 6 3.5a2.5 2.5 0 0 1 0 5z" fill="#ccc"/></svg><span>Tradolo, Suite 4, 18 Harbour Row<br>Bayview Point 4000</span></li>
        <li><svg width="12" height="14" viewBox="0 0 24 24"><path d="M6.6 10.8a15 15 0 0 0 6.6 6.6l2.2-2.2a1 1 0 0 1 1-.25 11.4 11.4 0 0 0 3.6.6 1 1 0 0 1 1 1V20a1 1 0 0 1-1 1A17 17 0 0 1 3 4a1 1 0 0 1 1-1h3.5a1 1 0 0 1 1 1c0 1.25.2 2.45.6 3.6a1 1 0 0 1-.25 1z" fill="#ccc"/></svg><span>Phone: 00 0 5550 1200<br>Fax: 00 0 5550 1900</span></li>
        <li><svg width="12" height="12" viewBox="0 0 24 24"><rect x="2" y="5" width="20" height="14" fill="#ccc"/><path d="M2 5l10 8 10-8" fill="none" stroke="#1d1e21" stroke-width="2"/></svg><span>info@tradolo.example</span></li>
      </ul>
    </div>
    <div class="col-links">
      <h4>Quick Links</h4>
      <ul><li>Home</li><li>About Us</li><li>How it Works</li><li>Our Services</li><li>Blog</li><li>Contact</li></ul>
    </div>
    <div class="col-brand">
      <span class="brand-dot"></span>
      <span class="brand-name">Tradolo</span>
      <div class="socials"><i></i><i></i><i></i><i></i></div>
    </div>
  </div>
  <div class="copyright">&copy;2016 - 2017 Tradolo. All Rights Reserved.</div>
</footer>

</body>
</html>
```